Resume: Professional Marketer seeking to impress potential recruiters with my skills & experience

Create a marketing esque style CV. I'm an outgoing, driven marketing with years of experience. I'm looking for a new senior role. My CV should look professional, but with elements of creativity and be a little bold. It should stand out amongst all the other CVs being submitted for a role. Check out my workfolio profile here: https://www.careerlinkspace.net/in/morwenna-traske-58291604/ I would like to include a photo with the design, as a subtle element of the design.

Target Market(s)

Recruiters, Headhunters

Industry/Entity Type

Marketing

Font styles to use
Sans Serif

Requirements
Must have
• Easy to read sections, with enough detail for a recruiter to understand my experience.
Nice to have
• Graphics, icons etc to represent experience

```html
<!DOCTYPE html>
<html lang="en">
<head>
<meta charset="utf-8">
<title>Resume – Experience and Qualifications</title>
<link rel="stylesheet" href="https://fonts.googleapis.com/css2?family=Libre+Caslon+Text:wght@400;700&family=Playfair+Display:wght@400;500&display=swap">
<style>
  :root {
    --canvas: #ffffff;
    --page: #e2d3c3;
    --page-light: #ece3d8;
    --band: #dccbb9;
    --divider: #eee6dc;
    --ink: #2b2622;
  }
  * { box-sizing: border-box; margin: 0; padding: 0; }
  html, body { width: 1200px; height: 850px; overflow: hidden; background: var(--canvas); }
  body {
    position: relative;
    font-family: "Libre Caslon Text", Georgia, serif;
    font-size: 10.6px;
    line-height: 13.6px;
    color: var(--ink);
  }
  .page { position: absolute; top: 12px; height: 828px; width: 585px; }
  .page--experience {
    left: 10px;
    background: linear-gradient(160deg, #e6d8c9 0%, var(--page) 50%, #dccbb8 100%);
  }
  .page--experience .divider {
    position: absolute; left: 0; right: 0; top: 374px; height: 14px; background: var(--divider);
  }
  .job { position: absolute; left: 40px; width: 520px; }
  .job--one { top: 75px; }
  .job--two { top: 419px; }
  .job-row { display: grid; grid-template-columns: 154px 1fr; }
  .job-row + .job-row { margin-top: 5px; }
  .job-title { margin-bottom: 0; }
  .duties { list-style: none; counter-reset: duty; margin-top: 3px; }
  .duties li { counter-increment: duty; position: relative; padding-left: 18px; margin-top: 3.3px; }
  .duties li::before { content: counter(duty) "."; position: absolute; left: 6px; }

  .page--qualifications { left: 606px; background: var(--page-light); }
  .quals-title {
    position: absolute; top: 100px; left: 0; right: 0; text-align: center;
    font-family: "Playfair Display", Georgia, serif; font-weight: 400; font-size: 20px; letter-spacing: .2px;
  }
  .band { position: absolute; left: 0; right: 0; background: var(--band); padding-left: 40px; }
  .band--degrees { top: 170px; height: 238px; }
  .band--education { top: 424px; height: 225px; }
  .band-heading { position: absolute; top: 20px; left: 40px; }
  .band--education .band-heading { top: 12px; }
  .qual-table { position: absolute; left: 40px; right: 0; }
  .band--degrees .qual-table { top: 47px; }
  .band--education .qual-table { top: 39px; }
  .qual-row {
    display: grid; grid-template-columns: 171px 171px 1fr;
    height: 39px; align-items: center;
  }
  .qual-row--head { height: 14px; margin-bottom: 13px; }
  .band--education .qual-row--head { margin-bottom: 18px; }
  .contact {
    position: absolute; top: 722px; left: 0; right: 0; text-align: center; line-height: 16.5px;
  }
</style>
</head>
<body>

<section class="page page--experience">
  <article class="job job--one">
    <div class="job-row">
      <span class="job-dates">January 2010 - October 2010</span>
      <span class="job-title">Product Portfolio Marketing Manager - CoverPoint<br>Part of the HARBOUR Group</span>
    </div>
    <div class="job-row">
      <span class="job-label">Role responsibilities:</span>
      <div>
        <p>The primary objectives of the Product Portfolio Marketing Manager - CoverPoint:</p>
        <ol class="duties">
          <li>To deliver product life cycle management of current and future planned CoverPoint products</li>
          <li>To direct the Marketing Managers and respective suppliers to achieve lead volumes at required cost metrics</li>
          <li>To actively manage a team of 4 Marketing Managers to achieve their objectives</li>
          <li>To communicate Marketing plans and objectives to key stakeholders within CoverPoint, from Senior Management to Call Centre Managers</li>
          <li>To prepare short, medium, and long term budgets. Analyse each quarter, reforecast, and accountability</li>
        </ol>
      </div>
    </div>
    <div class="job-row" style="margin-top:9px">
      <span class="job-label">Reporting to:<br>Key Relationships:</span>
      <span>Key stakeholder relationships with;<br>General Manager Marketing<br>Marketing Communications Manager<br>Digital Marketing Manager</span>
    </div>
  </article>

  <div class="divider"></div>

  <article class="job job--two">
    <div class="job-row">
      <span class="job-dates">January 2008 - October 2010</span>
      <span class="job-title">Marketing Manager<br>CoverPoint Pty Ltd</span>
    </div>
    <div class="job-row">
      <span class="job-label">Role responsibilities:</span>
      <div>
        <p>The primary objectives of the Marketing Manager:</p>
        <ol class="duties">
          <li>To Develop, monitor and implement acquisition strategy and plans including the introduction of new products cost effectively to market, inbound and outbound acquisition/upgrade/cross-sell activity</li>
          <li>Delivery of leads, profitability, product mix and channel targets by individual product and across the full product portfolio</li>
          <li>To develop and manage media strategy and new acquisition channel development to achieve leads and CPR requirements</li>
          <li>To identify and negotiate agreements with 3rd party channel partners for lead generation</li>
          <li>Manage all external media partners</li>
          <li>Report on marketing activity and results to the Senior Management team</li>
        </ol>
      </div>
    </div>
    <div class="job-row" style="margin-top:2px">
      <span class="job-label">Reporting to:<br>Key Relationships:</span>
      <span>Key stakeholder relationships with;<br>General Manager, Acquisition<br>Marketing Communications Manager<br>Digital Marketing Manager<br>Senior Management Team</span>
    </div>
  </article>
</section>

<section class="page page--qualifications">
  <h1 class="quals-title">QUALIFICATIONS:</h1>

  <div class="band band--degrees">
    <h2 class="band-heading" style="font:inherit">Degrees and Awards of relevance:</h2>
    <div class="qual-table">
      <div class="qual-row qual-row--head"><span>Institution</span><span>Degree</span><span>Dates</span></div>
      <div class="qual-row"><span>Harwood Institute of Technology, Sydney</span><span>Bachelor of Business, Major in Marketing and Small Business</span><span>January 1993 - June 1997</span></div>
      <div class="qual-row"><span>CoverPoint Pty Ltd</span><span>Employee of the Year<br>Award 2005</span><span>December 2005</span></div>
      <div class="qual-row"><span>Kestrel Limited</span><span>Outstanding Achievement<br>Award 2009</span><span>December 2008</span></div>
      <div class="qual-row"><span>Kestrel Limited</span><span>Overall Company Achievement<br>Award 2009</span><span>December 2009</span></div>
    </div>
  </div>

  <div class="band band--education">
    <h2 class="band-heading" style="font:inherit">Executive Education:</h2>
    <div class="qual-table">
      <div class="qual-row qual-row--head"><span>Institution</span><span>Program</span><span>Dates</span></div>
      <div class="qual-row"><span>Kestrel Limited</span><span>Kestrel Senior Leaders Strategy Program</span><span>April 2012 - Current</span></div>
      <div class="qual-row"><span>Kestrel Limited</span><span>Equip Leadership Program</span><span>February 2009 - April 2010</span></div>
      <div class="qual-row"><span>Lakeside Academy<br>Northgate, VIC</span><span>Certificate IV in Business,<br>Frontline Management</span><span>Completed October 2008</span></div>
    </div>
  </div>

  <p class="contact">For information on previous roles, please contact me at:<br>mtraske22@mailpost.com or 0400 555 118.</p>
</section>

</body>
</html>
```